Educational Agency in Abu Dhabi looking for an 8 pages website

We are looking for an 8 pages design for a website, we already have one but we need to refine it and it is www.kelvoranet.ae - Please base it on logo colours (attached) I have uploaded our logo, website content logo colors to use it for the scheme.
We are looking for a smooth look and content added if possible, I also attached content and logo

Industry/Entity Type

Education

Coding

Coded - Design and coding required

Number of Pages Required

5+ page

```html
<!DOCTYPE html>
<html lang="en">
<head>
<meta charset="utf-8">
<title>Kelvora Study</title>
<link rel="stylesheet" href="https://fonts.googleapis.com/css2?family=Roboto:wght@400;500;700&family=Barlow:wght@500;600;700&display=swap">
<style>
:root{
  --navy:#1f2f6b;
  --navy-deep:#1b2a5e;
  --royal:#4152b8;
  --royal-card:#4d5ec2;
  --cyan:#1a9fd8;
  --orange:#f7941d;
  --gold:#e9b92c;
  --ink:#1d2540;
  --text:#4a4f5c;
  --white:#ffffff;
  --footer:#2b2b2b;
}
*{box-sizing:border-box;margin:0;padding:0}
html,body{width:1200px;height:2961px;overflow:hidden;background:var(--white)}
body{font-family:"Roboto",Arial,sans-serif;color:var(--text);position:relative}
.page{position:relative;width:1200px;height:2961px;overflow:hidden}
.abs{position:absolute}

/* top bar & header */
.topbar{left:0;top:0;width:1200px;height:24px;background:var(--royal);display:flex;justify-content:flex-end;align-items:center;padding-right:170px;gap:20px}
.topbar a{color:#fff;font-size:10px;font-weight:500;text-decoration:none;text-transform:uppercase}
.header{left:0;top:24px;width:1200px;height:71px;background:#fff}
.logo{left:170px;top:38px;display:flex;align-items:center;gap:8px}
.logo-mark{width:28px;height:28px;background:var(--navy)}
.logo-name{font-family:"Barlow",sans-serif;font-weight:700;font-size:20px;color:var(--navy);letter-spacing:.5px}
.nav{right:235px;top:52px;display:flex;gap:17px}
.nav a{font-size:11px;font-weight:700;color:var(--ink);text-decoration:none;text-transform:uppercase}

/* hero */
.hero-photo{left:0;top:95px;width:1200px;height:560px;background:linear-gradient(100deg,#f5ede2 0%,#e9d6bd 30%,#c98f5a 55%,#4d6d9a 75%,#e2b357 100%)}
.hero-title{left:178px;top:254px;font-family:"Barlow",sans-serif;font-weight:700;font-size:36px;line-height:46px;color:var(--ink)}
.hero-band{left:0;top:560px;width:1200px}
.card{top:548px;width:270px;height:198px;padding:28px 34px;color:#fff}
.card h3{font-size:12px;font-weight:700;text-transform:uppercase;margin-bottom:8px}
.card p,.card li{font-size:10px;line-height:15px;list-style:none}
.card .more{position:absolute;left:34px;bottom:20px;font-size:11px;font-weight:500}
.card-partners{left:182px;background:var(--cyan)}
.card-partners .badge{position:absolute;right:28px;top:60px;width:50px;height:60px;background:#fff;opacity:.9}
.card-news{left:466px;background:var(--royal)}
.card-news h4{font-size:11px;font-weight:700;line-height:15px;margin-bottom:6px}
.card-apply{left:750px;background:var(--orange);display:flex;flex-direction:column;align-items:center;justify-content:center}
.card-apply h3{margin-bottom:14px}
.btn-small{background:#fff;color:var(--orange);font-size:10px;font-weight:700;padding:7px 24px;text-transform:uppercase}

/* destinations */
.section-title{width:1200px;left:0;text-align:center;font-family:"Barlow",sans-serif;font-weight:700;color:var(--ink)}
.dest-title{top:844px;font-size:28px}
.flags{left:180px;top:926px;display:flex;gap:25px}
.flag{width:83px;height:83px;border-radius:50%}

/* who */
.who-photo{left:178px;top:1074px;width:326px;height:244px;background:linear-gradient(135deg,#c9a06a,#e9d8c2 50%,#6b4a3a);transform:rotate(-1deg);box-shadow:-8px 8px 0 var(--navy)}
.who-text{left:553px;top:1078px;width:460px}
.who-text h2{font-family:"Barlow",sans-serif;font-weight:700;font-size:30px;color:var(--ink);margin-bottom:18px}
.who-text p{font-size:11px;line-height:15px;margin-bottom:10px}

/* why */
.why-bg{left:0;top:1300px;width:1200px;height:600px}
.why-title{top:1418px;font-size:28px;color:#fff}
.why-cards{left:178px;top:1490px;display:flex;gap:6px}
.why-card{width:206px;height:302px;background:var(--royal-card);text-align:center;padding-top:32px;color:#fff}
.why-icon{width:126px;height:126px;border-radius:50%;background:#fff;margin:0 auto 26px;display:flex;align-items:center;justify-content:center}
.why-card h3{font-size:14px;font-weight:700;margin-bottom:12px}
.why-card p{font-size:11px;line-height:15px;padding:0 18px}
.dots{left:560px;top:1832px;display:flex;gap:8px}
.dots span{width:36px;height:8px;border-radius:4px;background:rgba(255,255,255,.45)}
.dots span:first-child{background:#fff}

/* featured */
.feat-title{top:1946px;font-family:"Roboto",sans-serif;font-weight:400;font-size:22px;color:var(--cyan)}
.badges{left:230px;top:2024px;display:flex;gap:90px;align-items:center}
.badge-plain{width:112px;height:112px;background:#e7ebf3}

/* form */
.form-bg{left:0;top:2235px;width:1200px;height:363px;background:linear-gradient(90deg,#2c3e78,#24366d 40%,#1f3066)}
.form-photo{left:0;top:2235px;width:420px;height:363px;background:linear-gradient(110deg,#6f7fa8,#3f5288 60%,rgba(36,54,109,0))}
.form{left:494px;top:2282px;width:530px;color:#fff}
.form h2{font-family:"Roboto",sans-serif;font-weight:400;font-size:22px;text-transform:uppercase;margin-bottom:10px}
.form .lead{font-size:12px;margin-bottom:22px}
.field{border:1.5px solid rgba(255,255,255,.8);height:38px;font-size:10px;padding:11px 12px;color:#fff}
.field.active{border-color:var(--gold)}
.row{display:flex;gap:16px;margin-bottom:16px}
.row .field{width:166px}
.field.msg{width:530px;height:68px;margin-bottom:20px}
.btn-gold{display:inline-block;background:var(--gold);color:var(--ink);font-size:11px;font-weight:700;padding:12px 42px;text-transform:uppercase}

/* coach */
.coach-photo{left:197px;top:2620px;width:316px;height:237px;background:linear-gradient(120deg,#f0d8c0,#c74a3a 55%,#e9c9a3)}
.coach{left:513px;top:2688px;width:450px;text-align:center}
.coach h2{font-family:"Roboto",sans-serif;font-weight:400;font-size:20px;color:var(--ink);text-transform:uppercase;letter-spacing:.5px;margin-bottom:20px}
.coach-btns{display:flex;justify-content:center;gap:20px}
.btn{font-size:16px;color:#fff;padding:10px 0;width:166px;text-align:center}
.btn-blue{background:var(--cyan)}
.btn-orange{background:var(--orange)}

/* footer */
.footer{left:0;top:2857px;width:1200px;height:104px;background:var(--footer);padding:30px 178px;color:#9a9a9a}
.footer .copy{font-size:11px;color:#cfcfcf;margin-bottom:6px}
.footer p{font-size:9px;line-height:14px}
.social{right:178px;top:2890px;display:flex;gap:12px}
.social span{width:30px;height:30px;border-radius:50%;border:1.5px solid #9a9a9a}
.social span:nth-child(2){border-color:var(--cyan)}
</style>
</head>
<body>
<div class="page">

  <div class="abs topbar">
    <a>About Us</a><a>Apply Now</a><a>Contact Us</a><a>Study Destinations</a>
  </div>
  <div class="abs header"></div>
  <div class="abs logo"><span class="logo-mark"></span><span class="logo-name">KELVORA STUDY</span></div>
  <nav class="abs nav">
    <a>About Us</a><a>Why Study Abroad</a><a>Our Services</a><a>Courses</a><a>Study English Language</a><a>Scholarships</a>
  </nav>

  <div class="abs hero-photo" role="img" aria-label="Group of smiling students holding books and notebooks"></div>
  <h1 class="abs hero-title">You Academic<br>dreams is our<br>important choice</h1>

  <svg class="abs hero-band" width="1200" height="290" viewBox="0 0 1200 290" aria-hidden="true">
    <path d="M0 120 C300 60 700 40 1200 0 L1200 290 L0 290 Z" fill="var(--navy-deep)"/>
    <path d="M0 290 L0 250 C300 200 800 260 1200 170 L1200 290 Z" fill="#fff"/>
  </svg>

  <div class="abs card card-partners">
    <h3>Our Partners</h3>
    <ul>
      <li>Harrowgate University</li>
      <li><b>University of Ellsmere</b></li>
      <li>Northvale City University</li>
      <li>University of Carrick Bay</li>
      <li>University of Brenford</li>
      <li>University of Westmoor</li>
    </ul>
    <span class="badge"></span>
    <span class="more">Learn More</span>
  </div>
  <div class="abs card card-news">
    <h3>News &amp; Updates</h3>
    <h4>Open Education Resources Programs at Private Liberal Arts Institutions</h4>
    <p>12:00pm, Learning Commons, Viewing and Taking Room B Webinar with lunch provided. Private liberal arts institutions have been slow to address textbook affordability issues.</p>
    <span class="more">Learn More</span>
  </div>
  <div class="abs card card-apply">
    <h3>Make an Application</h3>
    <span class="btn-small">Apply Now</span>
  </div>

  <h2 class="abs section-title dest-title">Study Destinations</h2>
  <div class="abs flags">
    <span class="flag" role="img" aria-label="United Kingdom flag" style="background:#2b3f8f"></span>
    <span class="flag" role="img" aria-label="United States flag" style="background:#c8313e"></span>
    <span class="flag" role="img" aria-label="Australia flag" style="background:#1f3a93"></span>
    <span class="flag" role="img" aria-label="Malaysia flag" style="background:#d8343f"></span>
    <span class="flag" role="img" aria-label="European Union flag" style="background:#1f4aa8"></span>
    <span class="flag" role="img" aria-label="New Zealand flag" style="background:#213c8f"></span>
    <span class="flag" role="img" aria-label="China flag" style="background:#d9261c"></span>
    <span class="flag" role="img" aria-label="Germany flag" style="background:linear-gradient(#1a1a1a 33%,#d8262d 33% 66%,#f3c623 66%)"></span>
  </div>

  <div class="abs who-photo" role="img" aria-label="Graduate in cap and glasses"></div>
  <div class="abs who-text">
    <h2>Who we are?</h2>
    <p>KELVORA STUDY Abu Dhabi, one of the leading and fastest growing educational consulting company based in UAE officially recognized by the Higher Education Authority, Global Agency Network and QualityMark.</p>
    <p>Kelvora Study was established in 2015 with an aim to provide professional consultancy services for the recruitment of quality international students to educational institutions based in UK, USA, Canada, Australia, Malaysia, Germany, Europe, Middle East and many more.</p>
    <p>Our counseling services focus on student careers making sure that they are well placed in good and reputed institutions overseas.</p>
  </div>

  <svg class="abs why-bg" width="1200" height="600" viewBox="0 0 1200 600" aria-hidden="true">
    <path d="M0 60 C400 0 800 0 1200 40 L1200 600 L0 600 Z" fill="var(--royal)"/>
  </svg>
  <h2 class="abs section-title why-title">Why Kelvora Study?</h2>
  <div class="abs why-cards">
    <div class="why-card">
      <div class="why-icon"><svg width="44" height="44" viewBox="0 0 24 24"><path d="M4 22V6h7V2h9v20h-6v-4h-4v4z" fill="var(--royal)"/><g fill="#fff"><rect x="6" y="9" width="2" height="2"/><rect x="6" y="13" width="2" height="2"/><rect x="14" y="5" width="2" height="2"/><rect x="14" y="9" width="2" height="2"/><rect x="14" y="13" width="2" height="2"/></g></svg></div>
      <h3>Equipped Office</h3>
      <p>We have well-equipped office in ABU DHABI managed by an experienced team with counseling and good knowledge in overseas edu-</p>
    </div>
    <div class="why-card">
      <div class="why-icon"><svg width="44" height="44" viewBox="0 0 24 24"><rect x="4" y="3" width="16" height="19" rx="2" fill="var(--royal)"/><rect x="9" y="1" width="6" height="4" rx="1" fill="var(--royal)"/><g fill="#fff"><rect x="8" y="9" width="8" height="1.6"/><rect x="8" y="13" width="8" height="1.6"/><rect x="8" y="17" width="5" height="1.6"/></g></svg></div>
      <h3>Registration / License</h3>
      <p>KELVORA STUDY is registered with the Higher Education Authority and various government and private sectors.</p>
    </div>
    <div class="why-card">
      <div class="why-icon"><svg width="46" height="46" viewBox="0 0 24 24"><circle cx="12" cy="12" r="11" fill="var(--royal)"/><circle cx="12" cy="9" r="3.5" fill="#fff"/><path d="M5.5 18.5c1.5-3 4-4 6.5-4s5 1 6.5 4" fill="#fff"/></svg></div>
      <h3>Experienced Counselors</h3>
      <p>We have counselors with extensive experience to guide students to fit into the right universities.</p>
    </div>
    <div class="why-card">
      <div class="why-icon"><svg width="46" height="46" viewBox="0 0 24 24"><circle cx="12" cy="12" r="11" fill="var(--royal)"/><path d="M6.5 12.5l3.5 3.5 7.5-7.5" stroke="#fff" stroke-width="2.2" fill="none"/></svg></div>
      <h3>Quality of Counseling</h3>
      <p>We can assist with excellent, smart, smooth, and customized services for choosing the right course, getting admission, visa and arriving at the University.</p>
    </div>
  </div>
  <div class="abs dots"><span></span><span></span></div>

  <h2 class="abs section-title feat-title">AS FEATURED IN</h2>
  <div class="abs badges">
    <span class="badge-plain" style="background:#2f7fc7;border-radius:10px" role="img" aria-label="Agency certification badge"></span>
    <span class="badge-plain" style="border-radius:50%" role="img" aria-label="Education department emblem"></span>
    <span class="badge-plain" style="background:#eadccb;border-radius:50%" role="img" aria-label="Ministry emblem"></span>
    <span class="badge-plain" style="width:170px;height:60px;background:#d7e5f6" role="img" aria-label="Cultural council listing"></span>
  </div>

  <div class="abs form-bg"></div>
  <div class="abs form-photo" role="img" aria-label="Hands typing on a laptop"></div>
  <div class="abs form">
    <h2>Want to learn more?</h2>
    <p class="lead">Please Complete the form below</p>
    <div class="row">
      <div class="field active">Name *</div>
      <div class="field">Email *</div>
      <div class="field">Phone Number *</div>
    </div>
    <div class="field msg">Your message (Please tell us more about your child's needs, grade, and what you're hoping to accomplish.)</div>
    <span class="btn-gold">Register Now</span>
  </div>

  <div class="abs coach-photo" role="img" aria-label="Tutor helping a young girl with writing"></div>
  <div class="abs coach">
    <h2>Interested in becoming a coach?</h2>
    <div class="coach-btns">
      <span class="btn btn-blue">Contact Us</span>
      <span class="btn btn-orange">Apply Now</span>
    </div>
  </div>

  <footer class="abs footer">
    <div class="copy">© COPYRIGHT 2017, KELVORA STUDY</div>
    <p>CORNICHE TOWER, LEVEL 5 | ABU DHABI, UAE | PO BOX - 0000</p>
    <p>PHONE: +971 2 555 0142 | EMAIL: HELLO@KELVORANET.AE | WWW.KELVORANET.AE</p>
  </footer>
  <div class="abs social"><span></span><span></span><span></span><span></span></div>

</div>
</body>
</html>
```